Business Card Design

My company is a Consulting & Training company (Halvane Consulting and Training, LLC) specializing in Firearms Training, State of Florida Concealed Weapons Permit Course, and Tactical Equipment Consulting.

Industry/Entity Type

Business

Contact Information for Business Card

Dario Holtzmeyer
P.O. Box 417302
Aventura, FL 33917
(786)492-7318

```html
<!DOCTYPE html>
<html lang="en">
<head>
<meta charset="utf-8">
<title>Halvane Consulting and Training – Business Card</title>
<link rel="stylesheet" href="https://fonts.googleapis.com/css2?family=Orbitron:wght@500;700&display=swap">
<style>
  :root {
    --page: #ffffff;
    --camo-light: #4a4a4a;
    --camo-mid: #333333;
    --camo-dark: #1c1c1c;
    --red: #e5232b;
    --white: #f1f1f1;
    --card-shadow: rgba(0, 0, 0, 0.35);
  }
  * { box-sizing: border-box; margin: 0; padding: 0; }
  html, body {
    width: 1018px;
    height: 1200px;
    overflow: hidden;
    background: var(--page);
  }
  body {
    position: relative;
    font-family: "Orbitron", sans-serif;
    color: var(--white);
    text-transform: uppercase;
  }
  .card {
    position: absolute;
    left: 16px;
    width: 986px;
    height: 576px;
    overflow: hidden;
    box-shadow: 0 2px 6px var(--card-shadow);
  }
  .card--front { top: 15px; }
  .card--back { top: 607px; }
  .card__texture {
    position: absolute;
    inset: 0;
    background:
      radial-gradient(ellipse at 50% 45%, var(--camo-light) 0%, var(--camo-mid) 55%, var(--camo-dark) 100%);
  }
  .brand-mark {
    position: absolute;
    left: 50%;
    transform: translateX(-50%);
    background: var(--red);
  }
  .card--front .brand-mark { top: 110px; width: 110px; height: 110px; }
  .card--back .brand-mark { top: 80px; width: 90px; height: 90px; }

  .brand-name {
    position: absolute;
    left: 0;
    right: 0;
    text-align: center;
    font-weight: 500;
    color: var(--white);
  }
  .card--front .brand-name { top: 262px; }
  .brand-name__main {
    display: block;
    font-size: 62px;
    letter-spacing: 4px;
    line-height: 1.1;
  }
  .brand-name__sub {
    display: block;
    font-size: 27px;
    letter-spacing: 2px;
    line-height: 1.4;
  }
  .brand-name__llc {
    display: block;
    font-size: 20px;
    letter-spacing: 2px;
  }
  .card--back .brand-name {
    top: 196px;
    font-size: 20px;
    letter-spacing: 2px;
  }

  .holder-name {
    position: absolute;
    top: 296px;
    left: 0;
    right: 0;
    text-align: center;
    font-weight: 700;
    font-size: 50px;
    letter-spacing: 6px;
  }
  .holder-role {
    position: absolute;
    top: 356px;
    left: 0;
    right: 0;
    text-align: center;
    font-weight: 500;
    font-size: 23px;
    letter-spacing: 2px;
    color: var(--red);
  }
  .contact {
    position: absolute;
    font-weight: 500;
    font-size: 19px;
    letter-spacing: 2px;
    line-height: 25px;
    text-align: center;
  }
  .contact--postal { left: 46px; top: 458px; width: 300px; }
  .contact--direct { left: 500px; top: 472px; width: 440px; }
  .accent { color: var(--red); }
</style>
</head>
<body>
  <section class="card card--front">
    <div class="card__texture" role="img" aria-label="Dark grey digital camouflage fabric with horizontal webbing straps"></div>
    <div class="brand-mark"></div>
    <div class="brand-name">
      <span class="brand-name__main">Halvane</span>
      <span class="brand-name__sub">Consulting and Training</span>
      <span class="brand-name__llc">LLC</span>
    </div>
  </section>

  <section class="card card--back">
    <div class="card__texture" role="img" aria-label="Dark grey digital camouflage fabric with horizontal webbing straps"></div>
    <div class="brand-mark"></div>
    <div class="brand-name">Halvane Consulting and Training, LLC</div>
    <h1 class="holder-name">Dario Holtzmeyer</h1>
    <p class="holder-role">Owner/Operator</p>
    <address class="contact contact--postal" style="font-style:normal">
      P.O. Box <span class="accent">417302</span><br>
      Aventura<span class="accent">,</span> FL<br>
      <span class="accent">33917</span>
    </address>
    <p class="contact contact--direct">
      <span class="accent">(</span>786<span class="accent">)</span>492-7318<br>
      halvanect@fieldmail<span class="accent">.com</span>
    </p>
  </section>
</body>
</html>
```